STICKER DESIGN required for packaging. UK START UP TEA BUSINESS

We are looking for a design for a sticker that will be applied to packaging for our teas! We are a new start up Tea business based in the UK called 'BrookMints'
Selling quality loose leaf tea and teabags via our online shop and also face to face at farmers markets / food shows and eventually in our own tea emporium. We will be marketing our teas to hotels, cafes, delis etc. too
We carry every day teas eg. breakfast blends and also speciality and rare teas to offer customers the chance to try something new. Tea as a treat / ritual / indulgence / healthy lifestyle choice / modern
The design will initially be printed on vinyl stickers and then applied to the tea packaging (pouch bags in matte black and matte silver), in the future the design may be printed direct onto our packaging. The sticker design will need to be scalable as the size of the pouch bag varies dependant on the tea.
The sticker we have in mind is a leaf shape (sketch attached)
colour green to match our logo
It will include our logo (files attached)
Text to be included on the sticker is
- www.brookmints.co.uk
- Dellow, England
- The tea type eg. Green
It will need to complement both black and silver pouches that we are using to package our teas (see attached image of our pouches)
Colours - green leaf, see our corporate colours (green & orange) on our logo files attached. We also like silver and black.
Font - nothing to swirly, must be easy to read on the packaging
once a sticker design is agreed for the initial tea type (Green) we will require additional files for each tea type that we stock. Just the tea type (Green) to be updated - the rest of the design to stay the same. The tea types we stock are listed below
Green
Black
Oolong
White
Herbal
Blended
Happy to answer any questions and aim to give feedback daily! Thank you for your interest
Best regards

```html
<!DOCTYPE html>
<html lang="en">
<head>
<meta charset="utf-8">
<title>BrookMints Green – Leaf Sticker</title>
<link rel="stylesheet" href="https://fonts.googleapis.com/css2?family=Quicksand:wght@500;600&family=Bree+Serif&display=swap">
<style>
  :root {
    --page: #ffffff;
    --leaf: #044a22;
    --leaf-edge: #033d1c;
    --gold-light: #f6c44a;
    --gold-dark: #b8661e;
    --orange: #f7931e;
    --lime: #7cc242;
  }
  html, body {
    margin: 0;
    padding: 0;
    width: 820px;
    height: 1200px;
    overflow: hidden;
    background: var(--page);
  }
  .sticker-canvas {
    display: block;
    width: 820px;
    height: 1200px;
  }
  .leaf-body { fill: var(--leaf); stroke: var(--leaf-edge); stroke-width: 2; }
  .leaf-trim { fill: none; stroke: url(#goldTrim); stroke-width: 2.4; stroke-linejoin: round; }
  .curve-guide { fill: none; stroke: none; }
  .web-address {
    font-family: "Bree Serif", Georgia, serif;
    font-size: 20px;
    fill: var(--lime);
    letter-spacing: 0.5px;
  }
  .place-line {
    font-family: "Bree Serif", Georgia, serif;
    font-size: 20px;
    fill: var(--orange);
    letter-spacing: 0.5px;
  }
  .brand-name {
    font-family: "Quicksand", Arial, sans-serif;
    font-weight: 600;
    font-size: 40px;
    fill: var(--orange);
  }
  .brand-dot { fill: var(--lime); }
  .tea-type {
    font-family: "Quicksand", Arial, sans-serif;
    font-weight: 600;
    font-size: 28px;
    fill: var(--lime);
  }
  .tea-rule { stroke: var(--lime); stroke-width: 2.5; stroke-linecap: round; }
</style>
</head>
<body>
<svg class="sticker-canvas" viewBox="0 0 656 960" xmlns="http://www.w3.org/2000/svg" role="img" aria-label="Leaf-shaped sticker for BrookMints Green tea">
  <defs>
    <linearGradient id="goldTrim" x1="0" y1="0" x2="1" y2="1">
      <stop offset="0" stop-color="var(--gold-light)"/>
      <stop offset="0.5" stop-color="var(--gold-dark)"/>
      <stop offset="1" stop-color="var(--gold-light)"/>
    </linearGradient>
    <path id="webCurve" class="curve-guide" d="M166 500 C 190 430, 262 392, 372 372"/>
    <path id="placeCurve" class="curve-guide" d="M250 662 C 328 664, 392 634, 424 572"/>
  </defs>

  <g class="leaf">
    <path class="leaf-body" d="M180 648 C 120 610, 95 540, 125 470 C 170 370, 300 320, 430 320 C 500 320, 550 335, 578 345 C 520 370, 495 420, 475 500 C 455 580, 440 650, 400 690 C 340 700, 260 680, 210 662 L 160 775 C 154 790, 125 790, 120 772 Z"/>
    <path class="leaf-trim" d="M182 640 C 132 605, 112 540, 138 478 C 180 388, 302 338, 430 336 C 490 335, 530 340, 558 347 C 508 376, 487 428, 466 502 C 446 576, 432 640, 396 676 C 340 684, 266 666, 200 650 L 152 760 C 148 770, 134 770, 134 760 Z"/>
  </g>

  <text class="web-address"><textPath href="#webCurve">www.brookmints.co.uk</textPath></text>

  <g class="brand-lockup">
    <circle class="brand-dot" cx="300" cy="455" r="9"/>
    <text class="brand-name" x="300" y="538" text-anchor="middle">BrookMints</text>
  </g>

  <g class="tea-label">
    <line class="tea-rule" x1="213" y1="585" x2="236" y2="585"/>
    <text class="tea-type" x="293" y="594" text-anchor="middle">Green</text>
    <line class="tea-rule" x1="350" y1="585" x2="374" y2="585"/>
  </g>

  <text class="place-line"><textPath href="#placeCurve">Dellow, England</textPath></text>
</svg>
</body>
</html>
```